Oven Cleaning Business owner needs business card design

Hi there,
Would like for a business card to be designed for myself, the owner of a professional oven cleaning business on the Sunshine Coast.
Would like it to look sleek, and modern-ish. Bit creative is encouraged too.
Include following:
Name/title: Corin Haldegaard, Owner
Phone number: 1300 482 936
Email: info@glowrangeco.com.au
Website: www.glowrangeco.com.au

```html
<!DOCTYPE html>
<html lang="en">
<head>
<meta charset="utf-8">
<title>Glow Range Co — Business Card</title>
<link href="https://fonts.googleapis.com/css2?family=Montserrat:wght@500;600;800&display=swap" rel="stylesheet">
<style>
  :root {
    --cyan: #1bdedd;
    --ink: #000000;
    --card-light: #f1f1f1;
    --page: #fdfdfd;
    --white: #ffffff;
  }
  * { margin: 0; padding: 0; box-sizing: border-box; }
  html, body { width: 1200px; height: 1200px; overflow: hidden; background: var(--page); }
  body { position: relative; font-family: "Montserrat", sans-serif; }

  .card { position: absolute; left: 330px; width: 539px; height: 309px; overflow: hidden; }
  .card--front { top: 258px; background: var(--card-light); }
  .card--back { top: 634px; background: var(--ink); }

  .brand {
    position: absolute;
    display: flex; flex-direction: column; align-items: center; gap: 14px;
  }
  .card--front .brand { left: 173px; top: 72px; transform: translateX(-50%); }
  .card--back .brand { left: 270px; top: 70px; transform: translateX(-50%); }
  .brand__dot { width: 74px; height: 74px; border-radius: 50%; background: var(--cyan); }
  .brand__name {
    font-weight: 800; font-size: 26px; letter-spacing: 1px;
    color: var(--cyan); white-space: nowrap; text-transform: uppercase;
  }

  .person { position: absolute; right: 64px; top: 66px; text-align: right; }
  .person__name {
    font-weight: 500; font-size: 17px; letter-spacing: 0.6px;
    color: var(--cyan); line-height: 1; white-space: nowrap;
  }
  .person__title {
    font-weight: 600; font-size: 8.5px; letter-spacing: 0.4px;
    color: var(--ink); margin-top: 4px;
  }

  .contacts { position: absolute; right: 46px; top: 150px; list-style: none; }
  .contact {
    display: flex; align-items: center; justify-content: flex-end; gap: 7px;
    height: 25.7px; white-space: nowrap;
    font-weight: 500; font-size: 10.4px; letter-spacing: 0.5px; color: var(--cyan);
  }
  .contact__icon { width: 8px; height: 8px; display: block; flex: none; }
</style>
</head>
<body>

<section class="card card--front">
  <div class="brand">
    <span class="brand__dot"></span>
    <span class="brand__name">Glow Range Co</span>
  </div>

  <div class="person">
    <p class="person__name">Corin Haldegaard</p>
    <p class="person__title">Owner</p>
  </div>

  <ul class="contacts">
    <li class="contact">1300 482 936
      <svg class="contact__icon" viewBox="0 0 8 8"><rect width="8" height="8" rx="1" fill="#000"/><path d="M2 5.8 C2 3.5 3.5 2 5.8 2 L5.8 3.2 L4.8 3.4 C3.9 3.6 3.6 3.9 3.4 4.8 L3.2 5.8Z" fill="#fff"/></svg>
    </li>
    <li class="contact">info@glowrangeco.com.au
      <svg class="contact__icon" viewBox="0 0 8 8"><rect width="8" height="8" rx="1" fill="#000"/><rect x="1.6" y="2.3" width="4.8" height="3.4" fill="none" stroke="#fff" stroke-width="0.8"/><path d="M1.8 2.5 L4 4.2 L6.2 2.5" fill="none" stroke="#fff" stroke-width="0.7"/></svg>
    </li>
    <li class="contact">www.glowrangeco.com.au
      <svg class="contact__icon" viewBox="0 0 8 8"><rect width="8" height="8" rx="1" fill="#000"/><circle cx="4" cy="4" r="2.2" fill="none" stroke="#fff" stroke-width="0.9"/></svg>
    </li>
    <li class="contact">Sunshine Coast, QLD
      <svg class="contact__icon" viewBox="0 0 8 8"><rect width="8" height="8" rx="1" fill="#000"/><path d="M4 6.6 C2.6 5 2.2 4.2 2.2 3.5 A1.8 1.8 0 0 1 5.8 3.5 C5.8 4.2 5.4 5 4 6.6Z" fill="#fff"/><circle cx="4" cy="3.5" r="0.6" fill="#000"/></svg>
    </li>
  </ul>
</section>

<section class="card card--back">
  <div class="brand">
    <span class="brand__dot"></span>
    <span class="brand__name">Glow Range Co</span>
  </div>
</section>

</body>
</html>
```